New Dental Office Needs an Attractive and user friendly Website Designed

I need a website for a new dental office. The Name is Maplecrest Dentistry. I would like a Modern design with a user friendly interface and usability.
I would like a landing page, a page that lists the services we offer: Cosmetic Dentistry, Implants, Dental Hygiene, Emergency Services, Restorations, Dentures
Target Market(s)
Mid to upper class
Industry/Entity Type
Dentistry
Coding
Coded - Design and coding required
Number of Pages Required
1 page
Requirements
Must have
- Landing page that has a scheduling option, Procedures, operating hours, and contact us info
Nice to have
- Appealing design, Soft comforting colors. Easy to navigate page, Modern and professional.

```html
<!DOCTYPE html>
<html lang="en">
<head>
<meta charset="utf-8">
<title>Maplecrest Dentistry</title>
<link href="https://fonts.googleapis.com/css2?family=Outfit:wght@300;400;500;600&display=swap" rel="stylesheet">
<style>
:root{
  --green:#6dbf9a;
  --teal:#8dd0d8;
  --ink:#1f1f1f;
  --muted:#7a7a7a;
  --sand:#f5f4ef;
  --olive:#e3e1cd;
  --field:#e9e8e8;
  --white:#ffffff;
  --line:#dcdcdc;
  --leaf:#2a3a33;
}
*{box-sizing:border-box;margin:0;padding:0}
html,body{width:1200px;height:3542px;overflow:hidden}
body{font-family:"Outfit",sans-serif;color:var(--ink);background:var(--white);position:relative}
.abs{position:absolute}
.nowrap{white-space:nowrap}
.btn{position:absolute;display:flex;align-items:center;justify-content:center;gap:10px;border-radius:30px;color:var(--white);font-size:14px;font-weight:500;text-decoration:none;white-space:nowrap}
.btn svg{width:18px;height:12px}
.btn-green{background:var(--green)}
.btn-teal{background:var(--teal)}
.sprig{position:absolute;width:36px;height:28px;background:var(--leaf);border-radius:50% 50% 40% 40%}
/* header */
.brand{position:absolute;left:89px;top:38px;font-size:25px;font-weight:500;white-space:nowrap}
.nav{position:absolute;left:394px;top:44px;display:flex;gap:28px;font-size:14px;white-space:nowrap}
.nav a{color:var(--ink);text-decoration:none}
.nav a.active{border-bottom:2px solid var(--green);padding-bottom:4px}
.pill{position:absolute;top:29px;height:46px;border:1.5px solid var(--ink);border-radius:24px;display:flex;align-items:center;justify-content:center;font-size:13px;font-weight:600;white-space:nowrap}
/* hero */
.hero-title{left:87px;top:182px;font-size:86px;font-weight:600;line-height:.98;letter-spacing:-1px}
.hero-sub{left:90px;top:374px;font-size:33px;font-weight:400;white-space:nowrap}
.hero-photo{left:577px;top:120px;width:496px;height:452px;border-radius:248px 248px 0 0;background:linear-gradient(180deg,#e6f3f2,#bfe2e0)}
/* features */
.band-features{left:0;top:572px;width:1200px;height:498px;background:var(--sand);border-radius:80px}
.h2{font-size:38px;font-weight:500;letter-spacing:-.3px}
.card{position:absolute;top:740px;width:245px;height:236px;background:var(--white);border-radius:28px;text-align:center}
.card .icon{width:100px;height:100px;border-radius:50%;margin:22px auto 0;display:flex;align-items:center;justify-content:center}
.card h3{font-size:19px;font-weight:500;margin-top:16px}
.card p{font-size:14px;color:var(--muted);margin:8px auto 0;width:170px;line-height:1.4}
/* services */
.svc{position:absolute;left:613px;width:432px;height:100px;border-bottom:1px solid var(--line)}
.svc svg.ico{position:absolute;left:0;top:10px;width:54px;height:54px}
.svc h4{position:absolute;left:72px;top:2px;font-size:18px;font-weight:500;white-space:nowrap}
.svc p{position:absolute;left:72px;top:30px;width:310px;font-size:13px;color:var(--muted);line-height:1.5}
.svc .arr{position:absolute;right:0;top:28px;width:24px;height:16px}
/* cta */
.band-meet{left:0;top:1694px;width:1200px;height:497px;background:var(--sand);border-radius:80px}
.cta{left:89px;top:1625px;width:1022px;height:139px;background:var(--white);border-radius:70px;box-shadow:0 6px 30px rgba(0,0,0,.05)}
/* form */
.form-card{left:583px;top:2619px;width:469px;height:454px;background:var(--white);border-radius:28px;box-shadow:0 8px 40px rgba(0,0,0,.06)}
.field{position:absolute;height:52px;width:210px;background:var(--field);border-radius:26px;font-size:13px;font-weight:500;color:#555;padding:17px 28px}
/* footer */
.band-footer{left:0;top:3018px;width:1200px;height:524px;background:var(--olive);border-radius:80px 80px 0 0}
.foot-h{font-size:22px;font-weight:500;white-space:nowrap}
.foot-list{font-size:14px;line-height:32px}
.hours{font-size:14px;line-height:20px}
.dot{position:absolute;width:12px;height:12px;border-radius:50%;background:var(--green)}
.social{position:absolute;top:3198px;width:44px;height:44px;border-radius:50%;background:var(--white)}
.bottom-bar{left:43px;top:3437px;width:1115px;height:85px;background:var(--white);border-radius:43px;display:flex;align-items:center;justify-content:center;font-size:14px}
</style>
</head>
<body>

<!-- Header -->
<div class="brand">Maplecrest Dentistry</div>
<nav class="nav">
  <a class="active" href="#">Home</a><a href="#">About Us</a><a href="#">Services</a><a href="#">New Patients</a><a href="#">Contact</a>
</nav>
<div class="pill" style="left:825px;width:160px">Book Appointment</div>
<div class="pill" style="left:995px;width:116px">Book Now</div>

<!-- Hero -->
<div class="abs hero-photo" role="img" aria-label="Smiling patient in a light teal t-shirt against a soft circular backdrop"></div>
<h1 class="abs hero-title">Smile<br>Brighter</h1>
<p class="abs hero-sub">With Maplecrest Dentistry</p>
<a class="btn btn-green" style="left:98px;top:434px;width:207px;height:50px">Schedule Your Visit <svg viewBox="0 0 18 12" fill="none" stroke="#fff" stroke-width="1.6"><path d="M1 6h15M11 1l5 5-5 5"/></svg></a>
<a class="btn btn-teal" style="left:314px;top:434px;width:134px;height:50px">Call Now <svg viewBox="0 0 18 12" fill="none" stroke="#fff" stroke-width="1.6"><path d="M1 6h15M11 1l5 5-5 5"/></svg></a>

<!-- Features -->
<div class="abs band-features"></div>
<span class="sprig" style="left:582px;top:636px" role="img" aria-label="Small leaf ornament"></span>
<h2 class="abs h2" style="left:0;width:1200px;top:668px;text-align:center">Exceptional Care, Beautiful Results</h2>
<div class="card" style="left:89px"><div class="icon" style="background:var(--green)"><svg width="48" height="48" viewBox="0 0 48 48" fill="none" stroke="#fff" stroke-width="2"><circle cx="18" cy="18" r="9"/><path d="M26 22c4-3 12-2 12 6 0 5-3 8-4 14-2 0-3-6-6-6s-4 6-6 6c-1-5-3-8-3-12"/></svg></div><h3>Experienced Dentists</h3><p>Over 15 years of trusted care.</p></div>
<div class="card" style="left:349px"><div class="icon" style="background:var(--teal)"><svg width="48" height="48" viewBox="0 0 48 48" fill="none" stroke="#fff" stroke-width="2"><path d="M24 40S8 30 8 18a8 8 0 0 1 16-2 8 8 0 0 1 16 2c0 12-16 22-16 22z"/><circle cx="24" cy="20" r="4"/></svg></div><h3>Patient-Centered</h3><p>We treat you like a family.</p></div>
<div class="card" style="left:608px"><div class="icon" style="background:var(--green)"><svg width="48" height="48" viewBox="0 0 48 48" fill="none" stroke="#fff" stroke-width="2"><circle cx="24" cy="24" r="10"/><path d="M24 6v6M24 36v6M6 24h6M36 24h6M11 11l4 4M33 33l4 4M37 11l-4 4M15 33l-4 4"/></svg></div><h3>Advanced Technology</h3><p>Precision tools for modern care.</p></div>
<div class="card" style="left:867px"><div class="icon" style="background:var(--teal)"><svg width="48" height="48" viewBox="0 0 48 48" fill="none" stroke="#fff" stroke-width="2"><rect x="8" y="10" width="32" height="30" rx="4"/><path d="M8 18h32M16 6v8M32 6v8"/><circle cx="17" cy="26" r="3"/><circle cx="24" cy="26" r="3"/><circle cx="31" cy="26" r="3"/><circle cx="17" cy="34" r="3"/><circle cx="24" cy="34" r="3"/><circle cx="31" cy="34" r="3"/></svg></div><h3>Flexible Scheduling</h3><p>Evening &amp; weekend hours available.</p></div>

<!-- Services -->
<span class="sprig" style="left:154px;top:1170px" role="img" aria-label="Small leaf ornament"></span>
<h2 class="abs h2 nowrap" style="left:154px;top:1202px;font-size:36px;line-height:1.12">Comprehensive<br>Dental Services Under<br>One Roof</h2>
<p class="abs" style="left:154px;top:1336px;width:340px;font-size:13px;color:var(--muted);line-height:1.5">Feel free to get in touch with Maplecrest dentistry Clinic for general dentistry, specialist treatments or facial aesthetics.</p>
<a class="btn btn-green" style="left:154px;top:1416px;width:188px;height:50px">View All Services <svg viewBox="0 0 18 12" fill="none" stroke="#fff" stroke-width="1.6"><path d="M1 6h15M11 1l5 5-5 5"/></svg></a>

<div class="svc" style="top:1160px"><svg class="ico" viewBox="0 0 54 54" fill="none" stroke="var(--green)" stroke-width="1.6"><path d="M15 14c4-3 9-1 12 0 3-1 8-3 12 0 4 4 2 12 0 18-1 6-2 14-4 14-3 0-3-10-8-10s-5 10-8 10c-2 0-3-8-4-14-2-6-4-14 0-18z"/><path d="M8 8l2 2M46 8l-2 2M6 22h3"/></svg><h4>Cosmetic Dentistry</h4><p>Feel free to get in touch with Maplecrest dentistry Clinic for general dentistry, specialist...</p><svg class="arr" viewBox="0 0 24 16" fill="none" stroke="#999" stroke-width="1.4"><path d="M1 8h21M16 2l6 6-6 6"/></svg></div>
<div class="svc" style="top:1260px"><svg class="ico" viewBox="0 0 54 54" fill="none" stroke="var(--teal)" stroke-width="1.6"><circle cx="27" cy="27" r="24"/><path d="M18 18c3-2 6-1 9 0 3-1 6-2 9 0 3 3 1 9 0 13-1 4-2 9-3 9-2 0-2-6-6-6s-4 6-6 6c-1 0-2-5-3-9-1-4-3-10 0-13z"/></svg><h4>Dental Implants</h4><p>Feel free to get in touch with Maplecrest dentistry Clinic for general dentistry, specialist...</p><svg class="arr" viewBox="0 0 24 16" fill="none" stroke="#999" stroke-width="1.4"><path d="M1 8h21M16 2l6 6-6 6"/></svg></div>
<div class="svc" style="top:1360px"><svg class="ico" viewBox="0 0 54 54" fill="none" stroke="var(--green)" stroke-width="1.6"><path d="M13 8c5-4 10-1 14 0 4-1 9-4 14 0 5 5 2 15 0 22-1 8-3 18-5 18-4 0-4-12-9-12s-5 12-9 12c-2 0-4-10-5-18-2-7-5-17 0-22z"/><path d="M21 22h2M31 22h2M22 28c3 3 7 3 10 0"/></svg><h4>Dental Hygiene &amp; Cleanings</h4><p>Feel free to get in touch with Maplecrest dentistry Clinic for general dentistry, specialist...</p><svg class="arr" viewBox="0 0 24 16" fill="none" stroke="#999" stroke-width="1.4"><path d="M1 8h21M16 2l6 6-6 6"/></svg></div>
<div class="svc" style="top:1460px;border-bottom:none"><svg class="ico" viewBox="0 0 54 54" fill="none" stroke="var(--teal)" stroke-width="1.6"><circle cx="27" cy="27" r="24"/><path d="M18 18c3-2 6-1 9 0 3-1 6-2 9 0 3 3 1 9 0 13-1 4-2 9-3 9-2 0-2-6-6-6s-4 6-6 6c-1 0-2-5-3-9-1-4-3-10 0-13z"/></svg><h4>Emergency Dentistry</h4><p>Feel free to get in touch with Maplecrest dentistry Clinic for general dentistry, specialist...</p><svg class="arr" viewBox="0 0 24 16" fill="none" stroke="#999" stroke-width="1.4"><path d="M1 8h21M16 2l6 6-6 6"/></svg></div>

<!-- Meet + CTA -->
<div class="abs band-meet"></div>
<div class="abs" style="left:0;top:1860px;width:570px;height:331px;background:var(--white);border-radius:0 170px 170px 0;opacity:.7"></div>
<div class="abs" style="left:186px;top:1808px;width:433px;height:383px;background:linear-gradient(180deg,#e9dfd6,#f3f3f3 40%,#e4e6ea);border-radius:40px 40px 0 0" role="img" aria-label="Dentist in a white coat with a stethoscope, gesturing toward the text"></div>
<div class="abs cta">
  <h2 class="abs nowrap" style="left:78px;top:30px;font-size:38px;font-weight:500">Ready to Prioritize Your Smile?</h2>
  <p class="abs nowrap" style="left:80px;top:86px;font-size:14px;color:#555">Booking your visit is quick and easy. New patients welcome!</p>
  <a class="btn btn-green" style="left:651px;top:47px;width:165px;height:46px;font-size:13px">Book Appointment</a>
  <a class="btn btn-teal" style="left:826px;top:47px;width:117px;height:46px;font-size:12px">555 010 - 246</a>
</div>
<span class="sprig" style="left:668px;top:1882px" role="img" aria-label="Small leaf ornament"></span>
<h2 class="abs h2 nowrap" style="left:667px;top:1914px">Meet Your Dentist</h2>
<p class="abs" style="left:667px;top:1970px;width:350px;font-size:14px;color:var(--muted);line-height:1.45">My goal is to make every patient feel at home while receiving the highest quality care.</p>
<a class="btn btn-green" style="left:667px;top:2029px;width:268px;height:50px">Learn More About Our Team <svg viewBox="0 0 18 12" fill="none" stroke="#fff" stroke-width="1.6"><path d="M1 6h15M11 1l5 5-5 5"/></svg></a>

<!-- Testimonials -->
<span class="sprig" style="left:582px;top:2290px" role="img" aria-label="Small leaf ornament"></span>
<h2 class="abs h2" style="left:0;width:1200px;top:2322px;text-align:center">What Our Patients Are Saying</h2>
<p class="abs" style="left:200px;width:800px;top:2380px;text-align:center;font-size:19px;font-style:italic;font-weight:300;color:#777;line-height:1.4">Maplecrest Dentistry combines the latest technology with the kind of personalized care<br>that’s hard to find these days. They took the time to explain every procedure and made me feel<br>completely at ease.</p>
<p class="abs" style="left:0;width:1200px;top:2468px;text-align:center;font-size:13px;font-weight:500">Daniel R</p>
<div class="abs" style="left:579px;top:2508px;display:flex;gap:4px"><span style="width:12px;height:12px;border-radius:50%;background:#ccc"></span><span style="width:12px;height:12px;border-radius:50%;background:var(--green)"></span><span style="width:12px;height:12px;border-radius:50%;background:#ccc"></span></div>

<!-- Footer band (behind form) -->
<div class="abs band-footer"></div>

<!-- Contact -->
<h2 class="abs h2 nowrap" style="left:148px;top:2682px;line-height:1.08">Have a Question?<br>We’re Happy to Help.</h2>
<p class="abs" style="left:150px;top:2778px;width:340px;font-size:13px;color:var(--muted);line-height:1.5">Feel free to get in touch with Maplecrest dentistry Clinic for general dentistry, specialist treatments or facial aesthetics.</p>
<div class="abs form-card">
  <div class="field" style="left:20px;top:34px">First Name*</div>
  <div class="field" style="left:236px;top:34px">Last Name*</div>
  <div class="field" style="left:20px;top:100px">Email*</div>
  <div class="field" style="left:236px;top:100px">Phone*</div>
  <div class="field" style="left:20px;top:166px">Address*</div>
  <div class="field" style="left:236px;top:166px">Company*</div>
  <div class="field" style="left:20px;top:232px;width:426px;height:130px;padding-top:14px">Send Your Message*</div>
  <a class="btn btn-green" style="left:153px;top:376px;width:157px;height:50px">Submit Now <svg viewBox="0 0 18 12" fill="none" stroke="#fff" stroke-width="1.6"><path d="M1 6h15M11 1l5 5-5 5"/></svg></a>
</div>

<!-- Footer -->
<div class="abs nowrap" style="left:89px;top:3222px;font-size:32px;font-weight:500">Maplecrest Dentistry</div>
<h3 class="abs foot-h" style="left:471px;top:3146px">Quick Links</h3>
<ul class="abs foot-list" style="left:471px;top:3186px;list-style:none"><li>Home</li><li>About Us</li><li>Services</li><li>New Patients</li><li>Contact</li></ul>
<h3 class="abs foot-h" style="left:685px;top:3146px">Operating Hours</h3>
<span class="dot" style="left:686px;top:3199px"></span>
<p class="abs hours nowrap" style="left:710px;top:3192px">Mon – Fri :<br>8:00 AM – 6:00 PM</p>
<span class="dot" style="left:686px;top:3255px"></span>
<p class="abs hours nowrap" style="left:710px;top:3248px">Saturday :<br>9:00 AM – 2:00 PM</p>
<p class="abs hours nowrap" style="left:710px;top:3306px">Sunday :<br><span style="border-bottom:1.5px solid var(--green)">Closed</span></p>
<h3 class="abs foot-h" style="left:966px;top:3146px">Follow Us</h3>
<span class="social" style="left:962px;background:var(--green)" aria-label="Social profile"></span>
<span class="social" style="left:1015px" aria-label="Video channel"></span>
<span class="social" style="left:1068px" aria-label="Photo profile"></span>

<div class="abs bottom-bar">© 2025 Maplecrest Dentistry. All Rights Reserved.</div>
<div class="abs" style="left:1096px;top:3459px;width:42px;height:42px;border-radius:50%;background:var(--green);display:flex;align-items:center;justify-content:center"><svg width="14" height="16" viewBox="0 0 14 16" fill="none" stroke="#fff" stroke-width="1.6"><path d="M7 15V2M2 7l5-5 5 5"/></svg></div>

</body>
</html>
```